Merrow's Voyage Atlas Mobile App

We need a sleek new design for our new mobile app we are launching in the South Pacific. This app will be released for both Lumafone and Corvex. The app has already been developed and your new design will give it the finishing touch we need to release it to our audience. This will be the premiere tourism app for the South Pacific and will be advertised heavily in our successful print publications which are distributed internationally. We are looking for you to provide two designs (for two screens in our mobile app) for this competition. The selected winner will have the opportunity to design the remaining screens in our app and website as a separate contract.

Attached you will see a few of the screens that currently exist in our mobile app to give you a feel for the functionality. The two screens we want you to design for this competition are the main listing page and the category selection page. These two screens will be included in the uploaded files and will be clearly marked so you know what we are looking for.

Please feel free to reach out to us with any questions if you need any guidance in directing your designs. Show us something sleek, engaging, and ultimately something that will drive our users to want to engage with the businesses that are listed in the app.

Please see the uploaded files for a couple of our current designs, the two screens we want you to design for this competition, and a few samples of design ideas we like.

Best of Luck!

Target Market(s)

Travelers to the South Pacific

Industry/Entity Type

Travel Industry

Font styles to use
Serif
Sans Serif

Colors
0492cd
33a6d7
ec1f27
f04a50
85cae6
cee9f5
f59296
cedeed
fbd4d5

Requirements
Must have
• Clean, attractive design for the two screens mentioned in the brief.
Nice to have
• Icon sets, color guide, font selection
Should not have
• Project should not be too busy or incorporate too many different colors, styles, fonts, etc.

```html
<!DOCTYPE html>
<html lang="en">
<head>
<meta charset="utf-8">
<title>Merrow's Voyage Atlas – Category Selection</title>
<link href="https://fonts.googleapis.com/css2?family=Inter:wght@400;500;600;700&display=swap" rel="stylesheet">
<style>
  :root {
    --stage: #e9ecef;
    --screen-bg: #ffffff;
    --red: #ec1f27;
    --ink: #1d1d1f;
    --muted: #9a9a9a;
    --white: #ffffff;
    --sea-deep: #17676f;
    --sea-mid: #2f8f96;
    --sea-light: #6fb7b4;
    --sand: #c9c7bb;
    --card-shadow: rgba(0, 0, 0, 0.14);
  }
  * { box-sizing: border-box; margin: 0; padding: 0; }
  html, body { width: 1200px; height: 900px; overflow: hidden; }
  body {
    background: var(--stage);
    font-family: "Inter", "Helvetica Neue", Arial, sans-serif;
    position: relative;
  }
  .app-screen {
    position: absolute;
    left: 375px; top: 50px;
    width: 450px; height: 800px;
    background: var(--screen-bg);
    overflow: hidden;
    box-shadow: 0 10px 40px rgba(0,0,0,0.12);
  }
  .hero {
    position: absolute; left: 0; top: 0;
    width: 450px; height: 300px;
    background:
      linear-gradient(200deg, var(--sand) 0%, var(--sea-light) 22%, var(--sea-mid) 45%, var(--sea-deep) 100%);
  }
  .status-bar {
    position: absolute; left: 0; top: 0; width: 100%; height: 26px;
    color: var(--white); font-size: 13px; font-weight: 500;
    display: flex; align-items: center; justify-content: space-between;
    padding: 0 10px;
  }
  .status-left { display: flex; align-items: center; gap: 5px; position: relative; z-index: 1; }
  .signal { display: flex; gap: 2px; }
  .signal span { width: 6px; height: 6px; border-radius: 50%; background: var(--white); }
  .status-time { position: absolute; left: 0; right: 0; text-align: center; font-weight: 600; }
  .status-right { display: flex; align-items: center; gap: 5px; position: relative; z-index: 1; }
  .battery { width: 24px; height: 11px; border: 1px solid var(--white); border-radius: 3px; padding: 1px; }
  .battery i { display: block; width: 100%; height: 100%; background: var(--white); border-radius: 1px; }
  .search-bar {
    position: absolute; left: 18px; top: 40px; width: 414px; height: 54px;
    background: var(--white); border-radius: 3px;
    display: flex; align-items: center; gap: 14px; padding: 0 18px;
    color: var(--muted); font-size: 15px;
  }
  .toggle {
    position: absolute; right: 22px; top: 138px;
    width: 54px; height: 28px; border-radius: 14px; background: var(--white);
  }
  .toggle-knob {
    position: absolute; right: 2px; top: 2px; width: 24px; height: 24px;
    border-radius: 50%; background: var(--red);
    display: flex; align-items: center; justify-content: center;
  }
  .destination { position: absolute; left: 26px; top: 190px; color: var(--white); }
  .destination-title { font-size: 35px; font-weight: 700; letter-spacing: -0.3px; }
  .destination-area { margin-top: 8px; display: flex; align-items: center; gap: 7px; font-size: 16px; font-weight: 600; }
  .category-grid {
    position: absolute; left: 22px; top: 324px;
    display: grid; grid-template-columns: repeat(3, 124px); gap: 19px;
  }
  .category-card {
    height: 124px; background: var(--white);
    box-shadow: 0 3px 14px var(--card-shadow);
    display: flex; flex-direction: column; align-items: center; justify-content: center; gap: 14px;
    color: var(--ink); font-size: 13px; font-weight: 600;
  }
  .category-card svg { width: 52px; height: 52px; fill: var(--red); }
</style>
</head>
<body>
<main class="app-screen">
  <div class="hero" role="img" aria-label="Aerial photo of a turquoise lagoon and sandy beach with umbrellas"></div>

  <div class="status-bar">
    <div class="status-left">
      <div class="signal"><span></span><span></span><span></span><span></span><span></span></div>
      <span>Quillor</span>
      <svg width="15" height="11" viewBox="0 0 15 11"><path d="M7.5 11 0 3.2A10.8 10.8 0 0 1 15 3.2Z" fill="#fff"/></svg>
    </div>
    <div class="status-time">9:41 AM</div>
    <div class="status-right"><span>100%</span><div class="battery"><i></i></div></div>
  </div>

  <div class="search-bar">
    <svg width="20" height="20" viewBox="0 0 20 20"><circle cx="8" cy="8" r="6" fill="none" stroke="#1d1d1f" stroke-width="2.4"/><path d="M12.5 12.5 18 18" stroke="#1d1d1f" stroke-width="2.6" stroke-linecap="round"/></svg>
    <span>Search keywords here…</span>
  </div>

  <div class="toggle"><div class="toggle-knob">
    <svg width="12" height="10" viewBox="0 0 12 10"><path d="M1 5l3.5 3.5L11 1" fill="none" stroke="#fff" stroke-width="1.6"/></svg>
  </div></div>

  <div class="destination">
    <h1 class="destination-title">Cook Island</h1>
    <div class="destination-area">
      <svg width="12" height="16" viewBox="0 0 12 16"><path d="M6 0a6 6 0 0 0-6 6c0 4.5 6 10 6 10s6-5.5 6-10a6 6 0 0 0-6-6Z" fill="#ec1f27"/><circle cx="6" cy="6" r="2.3" fill="#fff"/></svg>
      <span>Rarotonga</span>
      <svg width="10" height="6" viewBox="0 0 10 6"><path d="M0 0h10L5 6Z" fill="#fff"/></svg>
    </div>
  </div>

  <section class="category-grid">
    <div class="category-card">
      <svg viewBox="0 0 52 52"><path d="M14 6h24v40H14Z M4 18h10v28H4Z M38 18h10v28H38Z"/><g fill="#fff"><rect x="18" y="11" width="4" height="5"/><rect x="24" y="11" width="4" height="5"/><rect x="30" y="11" width="4" height="5"/><rect x="18" y="20" width="4" height="5"/><rect x="24" y="20" width="4" height="5"/><rect x="30" y="20" width="4" height="5"/><rect x="18" y="29" width="4" height="5"/><rect x="30" y="29" width="4" height="5"/><rect x="22" y="37" width="8" height="9"/><rect x="7" y="23" width="4" height="4"/><rect x="7" y="31" width="4" height="4"/><rect x="41" y="23" width="4" height="4"/><rect x="41" y="31" width="4" height="4"/></g></svg>
      <span>Accommodation</span>
    </div>
    <div class="category-card">
      <svg viewBox="0 0 52 52"><path d="M12 12h28l5 12h3v16h-5v5h-6v-5H15v5H9v-5H4V24h3Z"/><path d="M14 16h24l3 8H11Z" fill="#fff"/><circle cx="11" cy="31" r="3" fill="#fff"/><circle cx="41" cy="31" r="3" fill="#fff"/><rect x="18" y="30" width="16" height="3" fill="#fff"/></svg>
      <span>Transportation</span>
    </div>
    <div class="category-card">
      <svg viewBox="0 0 52 52"><path d="M10 4h3v12h2V4h3v12h2V4h3v14a5 5 0 0 1-4 5v25h-5V23a5 5 0 0 1-4-5Z M32 4c6 3 8 11 7 20h-3v24h-5V4Z"/></svg>
      <span>Food &amp; Drink</span>
    </div>
    <div class="category-card">
      <svg viewBox="0 0 52 52"><circle cx="32" cy="9" r="4"/><path d="M23 16l8-2 5 8h6v4h-8l-3-4-5 5 5 5v10h-4v-8l-8-6Z"/><circle cx="12" cy="37" r="9" fill="none" stroke="#ec1f27" stroke-width="3.5"/><circle cx="40" cy="37" r="9" fill="none" stroke="#ec1f27" stroke-width="3.5"/></svg>
      <span>Activities</span>
    </div>
    <div class="category-card">
      <svg viewBox="0 0 52 52"><path d="M4 20 38 8l3 8a4 4 0 0 0 3 6l3 8-34 12-3-8a4 4 0 0 0-3-6Z"/><g stroke="#fff" stroke-width="2"><path d="M18 19l6 17" stroke-dasharray="3 2"/><path d="M27 22l10-3M28 26l10-3M29 30l6-2"/></g></svg>
      <span>Coupon</span>
    </div>
    <div class="category-card">
      <svg viewBox="0 0 52 52"><path d="M26 46 7 28A11 11 0 0 1 26 13a11 11 0 0 1 19 15Z"/></svg>
      <span>Favorites</span>
    </div>
    <div class="category-card">
      <svg viewBox="0 0 52 52"><circle cx="26" cy="26" r="23"/><rect x="23" y="22" width="6" height="17" fill="#fff"/><circle cx="26" cy="15" r="3.5" fill="#fff"/></svg>
      <span>Categories 7</span>
    </div>
    <div class="category-card">
      <svg viewBox="0 0 52 52"><circle cx="26" cy="26" r="23"/><rect x="23" y="22" width="6" height="17" fill="#fff"/><circle cx="26" cy="15" r="3.5" fill="#fff"/></svg>
      <span>Categories 8</span>
    </div>
    <div class="category-card">
      <svg viewBox="0 0 52 52"><circle cx="26" cy="26" r="23"/><rect x="23" y="22" width="6" height="17" fill="#fff"/><circle cx="26" cy="15" r="3.5" fill="#fff"/></svg>
      <span>Categories 9</span>
    </div>
  </section>
</main>
</body>
</html>
```